Zertifikat-Design für Bildungsträger im Bereich der Erwachsenenbildung
Zielgruppe
Talwerk Akademie - Zertifizierter Bildungsträger im Bereich der Erwachsenenbildung. Überwiegend Mitarbeiter in Unternehmen.
Aufgabenstellung
'Erstelle ein hochwertiges, modernes und exklusiv wirkendes Zertifikat für die Talwerk Akademie. Das Design soll professionell, minimalistisch und zugleich edel sein. Ziel ist es, ein Dokument zu gestalten, das den Eindruck vermittelt: 'Das ist das einzige und beste Zertifikat in der ganzen verdammten Welt.'
Das Zertifikat soll im Querformat (idealerweise DIN A4 horizontal) gestaltet werden. Der Inhalt soll zweisprachig (Deutsch und Englisch) dargestellt werden, klar gegliedert und typografisch hochwertig aufgebaut. Alle Inhalte sollten mittig ausgerichtet sein, mit gut erkennbarer visueller Hierarchie.
Der Haupttext lautet wie folgt:
'Talwerk Akademie gratuliert 'Name / Platzhalter' zum erfolgreichen Abschluss des Kurses 'Platzhalter' Datum, Unterschrift (siehe unten)
+englisch
'Talwerk Akademie hereby certifies that [Name of Participant / Placeholder] has successfully participated on 'date'.
Darunter sollen zwei stilisierte Unterschriften platziert werden – gerne von Hand gezeichnet oder elegant typografisch umgesetzt. Die Beschriftung unter den Unterschriften lautet: 'Leitung Talwerk Akademie'.
Ein zentrales Element ist das Hologramm. Muster das gelieferte Bild 'Hologramm.png'. Es muss deutlich sichtbar und hochwertig integriert werden. Die Aufschrift 'Talwerk' im Hologramm muss klar erkennbar sein. Idealer Platz wäre unten links oder rechts, eventuell mit einer leichten 3D-Anmutung oder Glanzeffekt.
Das gesamte Design muss der Corporate Identity der Talwerk Akademie entsprechen. Die verwendeten Farben sind: Hauptfarbe Dunkelblau (RGB 14, 32, 62), ergänzt durch Hellblau (RGB 241, 245, 250), ein zusätzliches Blau (RGB 65, 111, 174), Pink (RGB 140, 130, 227), Dunkellila (RGB 169, 97, 161), sowie Gelb (RGB 248, 216, 73) und Orange (RGB 220, 121, 70) für gezielte Akzente.
Als Schriftart ist ausschließlich Roboto zu verwenden. Der Name des Teilnehmers soll besonders hervorgehoben werden (z...

```html
<!DOCTYPE html>
<html lang="de">
<head>
<meta charset="utf-8">
<title>Teilnahmezertifikat – Talwerk Akademie</title>
<link href="https://fonts.googleapis.com/css2?family=Roboto:wght@300;400;500;700;900&family=Kaushan+Script&display=swap" rel="stylesheet">
<style>
  :root {
    --navy: #1a2340;
    --blue: #416fae;
    --ice: #eff3fa;
    --white: #ffffff;
    --rule: #8fa8d6;
    --ink: #000000;
    --line-grey: #8a8f99;
  }
  html, body { margin: 0; padding: 0; overflow: hidden; }
  body { width: 1200px; height: 849px; font-family: "Roboto", sans-serif; color: var(--navy); }
  .certificate {
    position: relative; width: 1200px; height: 849px; overflow: hidden;
    background: linear-gradient(to right, var(--ice) 0, var(--ice) 883px, var(--white) 883px);
  }
  .frame { position: absolute; inset: 0; }
  .brand {
    position: absolute; left: 102px; top: 104px; margin: 0;
    font-size: 17px; font-weight: 700; letter-spacing: 1.6px; color: var(--navy);
  }
  .title { position: absolute; left: 100px; top: 178px; margin: 0; font-weight: 300; line-height: 1; }
  .title .de { display: block; font-size: 61px; color: var(--navy); letter-spacing: -0.5px; }
  .title .en { display: block; font-size: 61px; color: var(--blue); margin-top: -3px; letter-spacing: -0.5px; }
  .seal {
    position: absolute; left: 800px; top: 126px; width: 208px; height: 208px; border-radius: 50%;
    background: radial-gradient(circle at 35% 35%, #bfe6f2 0%, #c9e3df 35%, #d9d3ea 70%, #c7c4e6 100%);
    box-shadow: 0 0 0 4px rgba(140,130,227,0.25);
  }
  .intro { position: absolute; left: 102px; top: 372px; margin: 0; font-size: 17px; }
  .intro .en { color: var(--blue); }
  .name-band {
    position: absolute; left: 102px; top: 438px; width: 1004px; height: 118px;
    background: repeating-linear-gradient(to bottom, var(--rule) 0, var(--rule) 1px, transparent 1px, transparent 4.6px);
    opacity: 0.9;
  }
  .participant {
    position: absolute; left: 136px; top: 448px; margin: 0;
    font-size: 89px; font-weight: 900; color: var(--ink); letter-spacing: -0.5px; line-height: 1;
  }
  .label {
    position: absolute; margin: 0; font-size: 11.5px; font-weight: 400; letter-spacing: 1.6px;
    text-transform: uppercase; color: var(--navy);
  }
  .label .en { color: var(--blue); }
  .label-name { left: 102px; top: 566px; }
  .field { position: absolute; top: 650px; width: 308px; height: 48px; border-bottom: 1px solid var(--line-grey); }
  .field-date { left: 102px; }
  .field-lead { left: 450px; }
  .field-lead2 { left: 798px; }
  .date { position: absolute; left: 0; bottom: 6px; margin: 0; font-size: 24px; font-weight: 300; }
  .signature {
    position: absolute; bottom: -6px; margin: 0;
    font-family: "Kaushan Script", cursive; font-size: 38px; color: var(--ink); white-space: nowrap;
  }
  .field-lead .signature { left: 16px; }
  .field-lead2 .signature { left: 22px; }
  .label-date { left: 102px; top: 706px; }
  .label-lead { left: 450px; top: 706px; }
</style>
</head>
<body>
<main class="certificate">
  <svg class="frame" width="1200" height="849" viewBox="0 0 1200 849" aria-hidden="true">
    <path d="M82 42 H1124 A42 42 0 0 0 1166 84 V768 A42 42 0 0 0 1124 810 H82 A42 42 0 0 0 42 768 V84 A42 42 0 0 0 82 42 Z"
          fill="none" stroke="#416fae" stroke-width="4.5"/>
  </svg>

  <p class="brand">LOGO TALWERK AKADEMIE</p>

  <h1 class="title">
    <span class="de">teilnahmezertifikat</span>
    <span class="en">certificate of attendance</span>
  </h1>

  <div class="seal" role="img" aria-label="Holografisches Siegel der Akademie"></div>

  <p class="intro">Wir gratulieren zum erfolgreichen Abschluss / <span class="en">We hereby certify the successful completion</span></p>

  <div class="name-band" aria-hidden="true"></div>
  <p class="participant">Max Mustermann</p>
  <p class="label label-name">Name / <span class="en">Name of participant</span></p>

  <div class="field field-date"><p class="date">16. November 2025</p></div>
  <div class="field field-lead"><p class="signature">H. Brandauer</p></div>
  <div class="field field-lead2"><p class="signature">L. Korff</p></div>

  <p class="label label-date">Datum / <span class="en">Date</span></p>
  <p class="label label-lead">Leitung / <span class="en">Head of Talwerk Akademie</span></p>
</main>
</body>
</html>
```